Business school needs a web design

Who We are:
KRVT is a small business school that offers programs in Project Management. The school is based in West Africa and welcomes students from the whole area. Our aim is to become one of the reference business schools in Africa.

Project Brief:
The site will include all informations relevant for different types of visitors that we have: actual and future students, companies, mass media, future employees, ect. It will present information about subscription, list of programs, presentation of the school and its team,etc.

What We want:
This competition is for Design only no coding! We need design for two pages.
We did some wireframing for the home page and the list of programs page. We made them just to show how we imagine the website would look like. But we encourage creative designs, so you don't have to stick to the wireframe models.

Sites We like:
http://www.ravenmoorcollege.example/
http://www.belvantis.example/fr/etudes.html
http://www.qtl.example/mba/Pages/default.aspx

Color schemes
The logo of the school is red and black. So the color scheme of the website should match that. For the rest, it is opened to your imagination.
Updates

The payment for the project is now garanteed. Good luck to you all !

Target Market(s)

The target market is diversified because we have students of different ages, also company representatives or employees that might visit the website for recruitment purposes. But the majority of our audience should be aged between 20 - 30 years.

Industry/Entity Type

Small Business

Requirements
Must have
• The design must include two pages: a home page and another interior page : might be the list of programs or any other page relevant to the domain. The Home page must include a slide show at the beginning.
The background page must be white.
Nice to have
• The use of flat design for this project is preferred.
The use of Pelican scaffold as a base for the design is an asset.

```html
<!DOCTYPE html>
<html lang="fr">
<head>
<meta charset="utf-8">
<title>KRVT – Ecole de management de projet</title>
<link href="https://fonts.googleapis.com/css2?family=Raleway:wght@400;500;600;700&family=Open+Sans:wght@400;600&display=swap" rel="stylesheet">
<style>
:root{
  --red:#b3191b;
  --red-dark:#8e1214;
  --red-text:#c42424;
  --ink:#1f1f1f;
  --body:#444;
  --link:#1f5fb0;
  --line:#d9d9d9;
  --footer:#2e3039;
  --footer-deep:#202127;
  --footer-text:#c9cbd1;
  --white:#fff;
}
*{box-sizing:border-box;margin:0;padding:0}
html,body{width:683px;height:1200px;overflow:hidden;background:var(--white)}
body{font-family:"Raleway",sans-serif;color:var(--body);font-size:6.6px;line-height:1.45}
.page{position:relative;width:683px;height:1200px}
.abs{position:absolute}
a{color:inherit;text-decoration:none}

/* header */
.brand{left:89px;top:12px;display:flex;align-items:center;gap:5px}
.brand-mark{width:14px;height:14px;background:var(--red)}
.brand-name{font-weight:700;font-size:15px;color:var(--ink);letter-spacing:.5px}
.utility{left:334px;top:0;height:22px;display:flex;border:1px solid #e2e2e2;border-top:none;background:#fafafa}
.utility a{font-size:6.3px;color:#333;padding:0 6px;line-height:21px;border-left:1px solid #e2e2e2}
.utility a:first-child{border-left:none}
.mainnav{left:175px;top:37px;display:flex;gap:9px;font-size:6.8px;font-weight:500;color:#222}
.search{left:508px;top:35px;width:83px;height:15px;border:1px solid #d5d5d5;font-size:6px;color:#555;padding:0 5px;line-height:13px}
.search svg{position:absolute;right:4px;top:3px}

/* hero */
.hero{left:0;top:60px;width:683px;height:256px;background:linear-gradient(180deg,#4b4e4b 0%,#6d6a63 45%,#3d3a37 100%)}
.hero-tag{font-family:"Open Sans",sans-serif;color:var(--white);font-size:13.5px;padding:0 10px;line-height:33px;left:89px}
.hero-tag.red{top:208px;width:188px;background:var(--red)}
.hero-tag.black{top:245px;width:226px;background:#151515}
.slider{left:286px;top:308px;width:110px;height:15px;border-radius:8px;background:linear-gradient(#f3f3f3,#cfcfcf);display:flex;align-items:center;justify-content:center;gap:3px;box-shadow:0 1px 2px rgba(0,0,0,.3)}
.slider i{width:4px;height:4px;border-radius:50%;background:#9a9a9a}
.slider i.on{background:#2c7fd0}
.slider b{position:absolute;font-size:6px;color:#777;font-weight:400;top:2px}

/* sections */
.h-section{font-size:11px;color:var(--red-text);font-weight:500}
.h-section .dark{color:var(--ink)}
.dotted{height:0;border-top:1px dashed #c9a0a0}
.intro{left:89px;top:374px;width:335px;color:#555}
.post{top:454px;width:99px}
.post .thumb{height:52px}
.post h4{font-size:6.6px;margin-top:13px;font-weight:400;color:#333}
.post h4 a{color:var(--link);font-weight:600}
.post p{margin-top:2px}
.post .by{font-style:italic;margin-top:3px}
.post .by a{color:var(--link)}
.btn-more{display:inline-block;margin-top:4px;border:1.5px solid var(--red);font-size:6.5px;color:#222;padding:0 6px;line-height:17px}
.video{left:89px;top:635px;width:335px;height:177px;background:linear-gradient(180deg,#8a7c60 0%,#6d5d45 55%,#3e342a 100%)}
.controls{left:108px;top:785px;width:297px;height:20px;background:rgba(30,32,36,.9);display:flex;align-items:center;padding:0 6px;gap:8px}
.progress{flex:1;height:4px;background:#555;position:relative}
.progress span{position:absolute;left:0;top:0;height:4px;width:24%;background:#2a9be0}
.progress em{position:absolute;left:24%;top:0;height:4px;width:42%;background:#777}
.hd{font:italic 700 7px "Open Sans",sans-serif;color:#2a9be0}
.more{font-size:6.6px;color:#222;text-decoration:underline}
.event{left:89px;width:335px;display:flex;gap:11px}
.date{width:26px;height:26px;background:var(--red);color:#fff;text-align:center;box-shadow:2px 2px 0 #7b0f10;flex:none}
.date b{display:block;font-size:10px;font-weight:500;line-height:14px;padding-top:1px}
.date small{display:block;font-size:5px;line-height:7px}
.event h5{font-size:8px;font-weight:500;color:var(--link)}

/* sidebar */
.news{left:443px;width:149px;display:flex;gap:7px}
.news .thumb{width:40px;height:40px;flex:none}
.news h6{font-size:6.6px;font-weight:500;color:var(--link)}
.news time{display:block;font-style:italic;font-weight:600;color:#222}
.panel{left:443px;width:149px;border:1px solid #ddd}
.panel-head{background:var(--red-dark);color:#fff;font-size:10.5px;height:27px;padding:0 10px;display:flex;align-items:center;gap:8px}
.roles{list-style:none;padding:4px 9px 6px}
.roles li{font-size:6.6px;color:#333;line-height:16.3px;border-bottom:1px dashed #cfcfcf}
.roles li:last-child{border-bottom:none}
.subscribe{display:flex;gap:5px;padding:13px 9px}
.subscribe .input{width:94px;height:21px;border:1px solid #c8c8c8;background:#f0f0f0;font-size:6.3px;color:#555;line-height:19px;padding-left:7px}
.subscribe .go{width:30px;height:21px;background:#2b2d33;color:#fff;font-size:6.5px;text-align:center;line-height:21px}

/* partners */
.partners{left:89px;top:1001px;width:503px;height:48px;border:1px solid #dcdcdc;display:flex;align-items:center;justify-content:space-around;padding:0 16px}
.partner{display:flex;align-items:center;gap:4px;font-size:9.5px;font-weight:700;color:#2a2a2a}
.partner i{width:8px;height:8px;background:#4a4a4a;border-radius:50%}
.arrow{position:absolute;top:15px;font-size:13px;color:#aaa}

/* footer */
.footer{left:0;top:1057px;width:683px;height:125px;background:var(--footer);border-top:2px solid #c9c9c9}
.fcol{top:1076px;color:var(--footer-text);font-size:6.3px}
.fcol h6{color:var(--red-text);font-size:6.5px;font-weight:700;margin-bottom:4px}
.fcol ul{list-style:none}
.fcol li{line-height:16px;border-bottom:1px dashed #4a4d57}
.fcol li:last-child{border-bottom:none}
.fcol p{line-height:11px}
.phone{display:flex;gap:5px;margin-top:3px}
.newsletter{display:flex;margin-top:6px}
.newsletter span{width:48px;height:15px;background:#8f9199}
.newsletter b{background:var(--red-dark);color:#fff;font-size:6.5px;font-weight:500;line-height:15px;padding:0 8px}
.social{display:flex;gap:6px;margin-top:30px}
.social i{width:16px;height:16px;border-radius:50%;background:#9a9ca4}
.bottombar{left:0;top:1182px;width:683px;height:18px;background:var(--footer-deep);color:#9a9ca4;font-size:5.8px;text-align:center;line-height:18px}
</style>
</head>
<body>
<div class="page">

  <header>
    <a class="brand abs" href="#"><span class="brand-mark"></span><span class="brand-name">KRVT</span></a>
    <nav class="utility abs">
      <a href="#">Repertoire du personnel</a><a href="#">Blogue</a><a href="#">Salle de presse</a><a href="#">Nous joindre</a><a href="#">Francais</a>
    </nav>
    <nav class="mainnav abs">
      <a href="#">A propos de l'KRVT</a><a href="#">Programmes et Formation</a><a href="#">Etudiants</a><a href="#">Nouvelles et Evenements</a><a href="#">Entreprises</a>
    </nav>
    <div class="search abs">Search...
      <svg width="8" height="8" viewBox="0 0 8 8"><circle cx="4.5" cy="3.5" r="2.5" fill="none" stroke="#c42424" stroke-width="1"/><line x1="2.7" y1="5.3" x2="0.8" y2="7.2" stroke="#c42424" stroke-width="1.2"/></svg>
    </div>
  </header>

  <section class="hero abs" role="img" aria-label="Photo d'un enseignant devant un tableau noir face à une salle d'étudiants"></section>
  <div class="hero-tag red abs">WELCOME TO OUR SITE</div>
  <div class="hero-tag black abs">BRIGHTEN YOUR FUTURE WITH US</div>
  <div class="slider abs"><b style="left:6px">‹</b><i></i><i class="on"></i><i></i><i></i><i></i><b style="right:6px">›</b></div>

  <main>
    <h2 class="h-section abs" style="left:89px;top:352px"><span>KRVT</span> <span class="dark">: devenez les gestionnaires de demain</span></h2>
    <p class="intro abs">Lorem ipsum dolor sit amet, consectetur adipisicing elit, sed do eiusmod tempor incididunt ut labore et dolore magna aliqua. Lorem ipsum dolor sit amet, consectetur adipisicing elit, sed do eiusmod tempor incididunt ut labore et dolore magna aliqua.</p>

    <h2 class="h-section abs" style="left:89px;top:421px">Blogue</h2>
    <div class="dotted abs" style="left:89px;top:442px;width:335px"></div>

    <article class="post abs" style="left:89px">
      <div class="thumb" role="img" aria-label="Photo de trois étudiants souriants" style="background:linear-gradient(135deg,#d8d4cf,#8a6f5c)"></div>
      <h4><a href="#">Title Name,</a> Nov 25 2013</h4>
      <p>Lorem ipsum dolor sit amet, consectetur adipisicing elit, sed do eiusmod tempor.</p>
      <p class="by">By, <a href="#">Me</a></p>
      <a class="btn-more" href="#">Lire la suite</a>
    </article>
    <article class="post abs" style="left:207px">
      <div class="thumb" role="img" aria-label="Photo d'une présentation en salle de cours" style="background:linear-gradient(135deg,#b8b3a6,#5d5348)"></div>
      <h4><a href="#">Title Name,</a> Nov 25 2013</h4>
      <p>Lorem ipsum dolor sit amet, consectetur adipisicing elit, sed do eiusmod tempor.</p>
      <p class="by">By, <a href="#">Me</a></p>
      <a class="btn-more" href="#">Lire la suite</a>
    </article>
    <article class="post abs" style="left:326px">
      <div class="thumb" role="img" aria-label="Photo d'étudiants présentant devant la classe" style="background:linear-gradient(135deg,#c9bfae,#4e4237)"></div>
      <h4><a href="#">Title Name,</a> Nov 25 2013</h4>
      <p>Lorem ipsum dolor sit amet, consectetur adipisicing elit, sed do eiusmod tempor.</p>
      <p class="by">By, <a href="#">Me</a></p>
      <a class="btn-more" href="#">Lire la suite</a>
    </article>

    <h2 class="h-section abs" style="left:89px;top:611px">KRVT Tv</h2>
    <div class="video abs" role="img" aria-label="Vidéo d'étudiants présentant un projet devant un tableau blanc"></div>
    <div class="controls abs">
      <svg width="20" height="14" viewBox="0 0 20 14"><rect width="20" height="14" fill="#1b1c20"/><polygon points="7,3 14,7 7,11" fill="#fff"/></svg>
      <div class="progress"><em></em><span></span></div>
      <span class="hd">HD</span>
      <svg width="7" height="7" viewBox="0 0 7 7"><path d="M0 0h2.5L0 2.5zM7 0v2.5L4.5 0zM0 7V4.5L2.5 7zM7 7H4.5L7 4.5z" fill="#ddd"/></svg>
    </div>
    <a class="more abs" href="#" style="left:89px;top:826px">De Videos &gt;&gt;</a>

    <h2 class="h-section abs" style="left:89px;top:850px">Evenements</h2>
    <div class="dotted abs" style="left:89px;top:870px;width:335px"></div>
    <div class="event abs" style="top:882px">
      <div class="date"><b>14</b><small>NOV</small></div>
      <div><h5>Event Headline</h5><p>Lorem ipsum dolor sit amet, consectetur adipisicing elit, sed do eiusmod tempor incididunt ut labore et dolore magna aliqua.</p></div>
    </div>
    <div class="event abs" style="top:925px">
      <div class="date"><b>31</b><small>DEC</small></div>
      <div><h5>Event Headline</h5><p>Lorem ipsum dolor sit amet, consectetur adipisicing elit, sed do eiusmod tempor incididunt ut labore et dolore magna aliqua.</p></div>
    </div>
    <a class="more abs" href="#" style="left:89px;top:970px">Tous les Eventements &gt;&gt;</a>
  </main>

  <aside>
    <h2 class="h-section abs" style="left:443px;top:351px">Nouvelles</h2>
    <div class="news abs" style="top:374px"><div class="thumb" role="img" aria-label="Photo d'étudiantes au travail" style="background:linear-gradient(135deg,#8c6a4e,#d9b48a)"></div><div><h6>Headline goes here</h6><p>Lorem ipsum dolor sit amet, consectetur adipisicing elit.</p><time>24 Nov, 2013</time></div></div>
    <div class="news abs" style="top:427px"><div class="thumb" role="img" aria-label="Photo d'un téléphone en main" style="background:linear-gradient(135deg,#a8744a,#e0c6a6)"></div><div><h6>Headline goes here</h6><p>Lorem ipsum dolor sit amet, consectetur adipisicing elit.</p><time>31 Dec, 2013</time></div></div>
    <div class="news abs" style="top:480px"><div class="thumb" role="img" aria-label="Photo d'un bureau avec des fleurs" style="background:linear-gradient(135deg,#3e3744,#bfb7c1)"></div><div><h6>Headline goes here</h6><p>Lorem ipsum dolor sit amet, consectetur adipisicing elit.</p><time>31 Dec, 2013</time></div></div>
    <div class="news abs" style="top:534px"><div class="thumb" role="img" aria-label="Photo d'étudiantes au travail" style="background:linear-gradient(135deg,#8c6a4e,#d9b48a)"></div><div><h6>Headline goes here</h6><p>Lorem ipsum dolor sit amet, consectetur adipisicing elit.</p><time>24 Nov, 2013</time></div></div>
    <div class="news abs" style="top:587px"><div class="thumb" role="img" aria-label="Photo d'un téléphone en main" style="background:linear-gradient(135deg,#a8744a,#e0c6a6)"></div><div><h6>Headline goes here</h6><p>Lorem ipsum dolor sit amet, consectetur adipisicing elit.</p><time>31 Dec, 2013</time></div></div>
    <div class="news abs" style="top:641px"><div class="thumb" role="img" aria-label="Photo d'un bureau avec des fleurs" style="background:linear-gradient(135deg,#3e3744,#bfb7c1)"></div><div><h6>Headline goes here</h6><p>Lorem ipsum dolor sit amet, consectetur adipisicing elit.</p><time>31 Dec, 2013</time></div></div>
    <a class="more abs" href="#" style="left:443px;top:694px">De Nouvelles &gt;&gt;</a>

    <section class="panel abs" style="top:719px">
      <div class="panel-head">Vous etes
        <svg width="14" height="10" viewBox="0 0 14 10"><rect x="1" y="3" width="7" height="4" rx="2" fill="none" stroke="#fff" stroke-width="1.4" transform="rotate(-30 4.5 5)"/><rect x="6" y="3" width="7" height="4" rx="2" fill="none" stroke="#fff" stroke-width="1.4" transform="rotate(-30 9.5 5)"/></svg>
      </div>
      <ul class="roles">
        <li>Futur etudiant</li><li>Etudiant actuel</li><li>Entreprise</li><li>Employeur</li><li>Postulant</li><li>Medias</li><li>Partenaires</li>
      </ul>
    </section>

    <section class="panel abs" style="top:893px">
      <div class="panel-head">Subscribe Us
        <svg width="13" height="9" viewBox="0 0 13 9"><rect x=".5" y=".5" width="12" height="8" fill="none" stroke="#fff"/><polyline points=".5,.5 6.5,5 12.5,.5" fill="none" stroke="#fff"/></svg>
      </div>
      <div class="subscribe"><span class="input">Your Email id...</span><span class="go">Go</span></div>
    </section>
  </aside>

  <section class="partners abs">
    <span class="arrow" style="left:6px">‹</span>
    <span class="partner"><i></i>Orvane</span>
    <span class="partner"><i></i>Tellwick</span>
    <span class="partner"><i></i>Brightmarket</span>
    <span class="partner"><i></i>Solenne</span>
    <span class="partner"><i></i>Harrowgate</span>
    <span class="partner"><i></i>Kestrel</span>
    <span class="arrow" style="right:6px">›</span>
  </section>

  <footer>
    <div class="footer abs"></div>
    <div class="fcol abs" style="left:89px;width:84px">
      <h6>A propos</h6>
      <ul><li>A propos de l'KRVT</li><li>Admissions</li><li>Calendrier de l'emploi</li><li>Repertoire du personnel</li></ul>
    </div>
    <div class="fcol abs" style="left:191px;width:84px">
      <h6>Etudiants</h6>
      <ul><li>Accueil - Etudiants</li><li>Programmes et Formations</li><li>Vie etudiante</li></ul>
      <h6 style="margin-top:4px;margin-bottom:1px">Entreprises</h6>
      <h6>Blogue</h6>
    </div>
    <div class="fcol abs" style="left:295px;width:85px">
      <h6>KRVT</h6>
      <p>12, Rue des Baobabs<br>Quartier Nord, pres de la<br>Place du Marche<br>du Centre</p>
      <div class="phone">
        <svg width="10" height="12" viewBox="0 0 10 12"><path d="M2 0.5 L4 3 L3 4.5 Q4 7 6 8.5 L7.5 7.5 L9.8 9.5 L8 11.5 Q3 10 0.5 3 Z" fill="#9a9ca4"/></svg>
        <p>(000) 33 555 01 20<br>(000) 77 555 01 38</p>
      </div>
    </div>
    <div class="fcol abs" style="left:401px;width:90px">
      <h6>Infolettre</h6>
      <p>Recevez les dernieres<br>nouvelles de l'KRVT,<br>ainsi que les ressources<br>utiles sur le management<br>de projet.</p>
      <div class="newsletter"><span></span><b>Envoyer</b></div>
    </div>
    <div class="fcol abs" style="left:507px;width:85px">
      <h6>Suivez-nous</h6>
      <div class="social"><i></i><i></i><i></i><i></i></div>
    </div>
    <div class="bottombar abs">© KRVT, 2014 Tous droits reserves</div>
  </footer>

</div>
</body>
</html>
```